Design for a Service-Based Estimate

We want a design for an Estimate that will always be sent in PDF format. The estimate or proposal is a critical document that needs to plainly show the service items, item description but also needs to be attractive and professional looking. Our current estimate deliverable is attached but it looks really basic like a Word document

```html
<!DOCTYPE html>
<html lang="en">
<head>
<meta charset="utf-8">
<title>Service Estimate</title>
<link rel="stylesheet" href="https://fonts.googleapis.com/css2?family=Open+Sans:wght@400;600;700&display=swap">
<style>
  :root {
    --backdrop: #4a4a4c;
    --paper: #ffffff;
    --ink: #231f20;
    --rule: #231f20;
    --header-fill: #e6e7e8;
  }
  * { box-sizing: border-box; margin: 0; padding: 0; }
  html, body { width: 1200px; height: 800px; overflow: hidden; }
  body {
    background: var(--backdrop);
    font-family: "Open Sans", Arial, sans-serif;
    color: var(--ink);
    position: relative;
  }
  .page {
    position: absolute;
    background: var(--paper);
  }
  .page--estimate { left: 56px; top: 35px; width: 514px; height: 727px; }
  .page--terms { left: 635px; top: 38px; width: 512px; height: 724px; }

  .field-label {
    position: absolute;
    font-size: 9.5px;
    font-weight: 700;
    white-space: nowrap;
  }
  .bid-number { left: 31px; top: 27px; }
  .bid-date { left: 341px; top: 27px; }

  .recipient-field {
    position: absolute;
    left: 29px;
    width: 454px;
    display: flex;
    align-items: flex-end;
    font-size: 9.5px;
    font-weight: 700;
  }
  .recipient-field .blank {
    flex: 1;
    border-bottom: 0.8px solid var(--rule);
    margin-left: 4px;
    height: 9px;
  }
  .recipient-field--issued { top: 58px; }
  .recipient-field--address { top: 83px; }
  .recipient-field--contact { top: 108px; }

  .line-items {
    position: absolute;
    left: 28px;
    top: 145px;
    width: 458px;
    border-collapse: collapse;
    table-layout: fixed;
    font-size: 9px;
  }
  .line-items th, .line-items td {
    border: 0.8px solid var(--rule);
  }
  .line-items th {
    background: var(--header-fill);
    height: 53px;
    font-weight: 600;
    vertical-align: top;
    padding-top: 12px;
    line-height: 16px;
  }
  .line-items .currency { display: block; font-weight: 400; }
  .line-items tbody td { height: 26.6px; }
  .line-items .total-row td { height: 27px; }
  .line-items .total-label {
    text-align: right;
    font-weight: 600;
    padding-right: 15px;
    vertical-align: top;
    padding-top: 4px;
    border-right: none;
  }

  .terms-title {
    position: absolute;
    top: 41px;
    left: 0;
    width: 512px;
    text-align: center;
    font-size: 10.5px;
    font-weight: 400;
  }
  .terms-list {
    position: absolute;
    left: 76px;
    top: 71px;
    width: 376px;
    font-size: 6.6px;
    line-height: 11.6px;
    list-style: none;
  }
  .terms-list li { position: relative; }
  .terms-list li::before {
    content: "";
    position: absolute;
    left: -8px;
    top: 4.5px;
    width: 3px;
    height: 3px;
    border-radius: 50%;
    background: var(--ink);
  }
  .sign-date {
    position: absolute;
    left: 79px;
    top: 320px;
    font-size: 9.5px;
    font-weight: 700;
  }
  .signature-line {
    position: absolute;
    left: 313px;
    top: 325px;
    width: 121px;
    border-top: 0.8px solid var(--rule);
  }
  .signature-caption {
    position: absolute;
    left: 313px;
    width: 121px;
    top: 330px;
    text-align: center;
    font-size: 9.5px;
    font-weight: 700;
  }
</style>
</head>
<body>
  <section class="page page--estimate">
    <div class="field-label bid-number">Bid # :</div>
    <div class="field-label bid-date">Date :</div>

    <div class="recipient-field recipient-field--issued">Issued to<span class="blank"></span></div>
    <div class="recipient-field recipient-field--address">Address<span class="blank"></span></div>
    <div class="recipient-field recipient-field--contact">Contact Details<span class="blank"></span></div>

    <table class="line-items">
      <colgroup>
        <col style="width:193px"><col style="width:55px"><col style="width:52px"><col style="width:57px"><col style="width:101px">
      </colgroup>
      <thead>
        <tr>
          <th>Item</th>
          <th>Qnty.</th>
          <th>U/M</th>
          <th>Unit price<span class="currency">$</span></th>
          <th>Total<span class="currency">$</span></th>
        </tr>
      </thead>
      <tbody>
        <tr><td></td><td></td><td></td><td></td><td></td></tr>
        <tr><td></td><td></td><td></td><td></td><td></td></tr>
        <tr><td></td><td></td><td></td><td></td><td></td></tr>
        <tr><td></td><td></td><td></td><td></td><td></td></tr>
        <tr><td></td><td></td><td></td><td></td><td></td></tr>
        <tr><td></td><td></td><td></td><td></td><td></td></tr>
        <tr><td></td><td></td><td></td><td></td><td></td></tr>
        <tr><td></td><td></td><td></td><td></td><td></td></tr>
        <tr><td></td><td></td><td></td><td></td><td></td></tr>
        <tr><td></td><td></td><td></td><td></td><td></td></tr>
        <tr><td></td><td></td><td></td><td></td><td></td></tr>
        <tr><td></td><td></td><td></td><td></td><td></td></tr>
        <tr><td></td><td></td><td></td><td></td><td></td></tr>
        <tr><td></td><td></td><td></td><td></td><td></td></tr>
        <tr><td></td><td></td><td></td><td></td><td></td></tr>
        <tr><td></td><td></td><td></td><td></td><td></td></tr>
        <tr><td></td><td></td><td></td><td></td><td></td></tr>
        <tr class="total-row">
          <td class="total-label" colspan="4">Total</td>
          <td></td>
        </tr>
      </tbody>
    </table>
  </section>

  <section class="page page--terms">
    <h2 class="terms-title">Terms and Conditions</h2>
    <ul class="terms-list">
      <li>Prices as quoted in this estimate are valid for (60) days only.</li>
      <li>Payment in full, less any previously paid amounts, is due to the Contractor upon completion of the proposed scope of work.</li>
      <li>All change order requests must be communicated in writing to the Contractor by the Client or their authorized representative.</li>
      <li>All measurements listed in this estimate are approximate and may vary slightly due to actual field conditions.</li>
      <li>It is agreed by the Contractor and the Client that complications and costs arising from unforeseen conditions and handling of unsuitable materials are not included in this estimate.</li>
      <li>Unless specifically listed in this estimate, the following items and their costs are not included: Maintenance of Traffic, Concrete Material Pumping, Testing, Excavation, Grading and Fill Material, Permits and Fees, Surveying and As-builts, Irrigation Repair, Landscaping and Root Mitigation, De-watering, Private Locates and Accessibility.</li>
      <li>Private utility locating services using radio detection devices and, when necessary, ground penetrating radar are offered by Firmline Paving to assist in finding private utilities that may not have been located by the public one call system. Firmline Paving will not be responsible for private utilities that have not been located nor for the failure of the above equipment to accurately detect existing utilities since the equipment is fallible and existing site conditions may preclude the ability of the equipment to detect an identifiable signal.</li>
    </ul>
    <div class="sign-date">Date :</div>
    <div class="signature-line"></div>
    <div class="signature-caption">Client Signature</div>
  </section>
</body>
</html>
```